Motivational Quotes Poster Series

This is a 3 poster design series for Ridgeway Haul Academy. The size of each poster should be 18 inches wide and 24 inches tall. The goal of these posters is to serve as motivational "signs" to be hung in the office area for the employees (not customers). These employees are instructors/teachers, teaching students how to drive semi trucks. While each design is a separate poster and design, we're posting as 1 project because we'd like some continuity between the series. Below we'll break down the details of all 3 posters...

Poster #1
Text that must appear on poster - "If You Want The Best Out Of Each Student" and "Give The Best Of You!" Note: While this text must appear on the poster, you can arrange in the layout as you see fit. For example, first line could be at top of poster and second line on bottom.

Poster #2
Text that must appear on poster - "Invest In People" and "Change Someone's Life" (same notes apply as in 1st poster)

Poster #3
Text that must appear on poster - "Today Is..." and "Just Another Day For You" and "The Most Important Day In Their Life" Note: This can be laid out on the poster however you see fit, but each phrase needs to be separate and it needs to flow.

Target Market(s)

Truck Driver Training Instructors - These are middle-aged, mostly male, masculine type personalities.

Industry/Entity Type

Training

Requirements
Must have
• Must have noted text from description
Must have working files (ie - PSD, EPS, AI, etc) provided
Must have common theme between each poster in series
Must have easy to read font and layout
Must have product dimensions of 18 inches (width) by 24 inches (height). If design uses full dimensions please include quarter inch bleed.
Nice to have
• Nice to have a trucking theme...related to trucking industry, but not over the top. Example - This could mean subtle injection of background tire tracks, but by no means are tire tracks required.

For inspiration, you can visit the site at http://www.ridgewayhaulacademy.com. While you can use the colors of the site/logo, you can still branch out between each poster to try new colors within reason.

Note: While we've attached the logo to this project, it COULD be used but doesn't HAVE to be included in the design. The logo IS NOT a focal point. The phrases in the poster ARE the focal point.

```html
<!DOCTYPE html>
<html lang="en">
<head>
<meta charset="utf-8">
<title>Today Is… — Ridgeway Haul Academy</title>
<link href="https://fonts.googleapis.com/css2?family=Oswald:wght@500;600;700&family=Patrick+Hand+SC&family=Parisienne&display=swap" rel="stylesheet">
<style>
  :root {
    --frame: #d9d9d9;
    --paper: #ffffff;
    --sky-top: #dcdcdc;
    --red: #e0262b;
    --green: #8dc03f;
    --blue: #1f7fc4;
    --dash: #3aa0db;
    --maroon: #9b1a1f;
    --violet: #9a7bb0;
    --ink: #333333;
    --stripe: #b8dcf2;
    --placeholder-a: #e4e7ec;
    --placeholder-b: #cfd6df;
  }
  * { margin: 0; padding: 0; box-sizing: border-box; }
  html, body { width: 900px; height: 1200px; overflow: hidden; background: var(--frame); }
  .poster {
    position: relative;
    width: 900px; height: 1200px;
    border: 9px solid var(--frame);
    background: linear-gradient(to bottom, var(--sky-top) 0, #f2f2f2 200px, var(--paper) 290px);
    overflow: hidden;
  }
  .line { position: absolute; white-space: nowrap; line-height: 1; }
  .today {
    left: 225px; top: 100px;
    font-family: "Oswald", sans-serif; font-weight: 600;
    font-size: 100px; color: var(--red); letter-spacing: 2px;
  }
  .today .is {
    font-family: "Patrick Hand SC", cursive; font-weight: 400;
    font-size: 72px; margin-left: 34px; letter-spacing: 6px;
  }
  .just {
    left: 150px; top: 358px;
    font-family: "Oswald", sans-serif; font-weight: 600;
    font-size: 82px; color: var(--green);
  }
  .just .rest {
    font-family: "Patrick Hand SC", cursive; font-weight: 400;
    font-size: 52px; color: var(--ink); margin-left: 18px; letter-spacing: 1.5px;
  }
  .divider { position: absolute; left: 160px; top: 478px; width: 590px; height: 6px; }
  .most {
    right: 117px; top: 528px;
    font-family: "Oswald", sans-serif; font-weight: 700;
    font-size: 92px; color: var(--blue);
  }
  .important {
    left: 150px; top: 632px;
    font-family: "Oswald", sans-serif; font-weight: 700;
    font-size: 68px; color: var(--maroon);
  }
  .life {
    left: 270px; top: 722px;
    font-family: "Parisienne", cursive;
    font-size: 100px; color: var(--violet);
  }
  .brand {
    position: absolute; left: 676px; top: 972px;
    display: flex; align-items: center; gap: 8px;
    font-family: "Oswald", sans-serif; font-weight: 500;
    font-size: 16px; line-height: 1.05; color: var(--ink);
  }
  .brand .mark { width: 26px; height: 26px; background: var(--ink); }
  .stripes { position: absolute; left: 0; top: 1028px; width: 882px; height: 72px; }
  .truck-art {
    position: absolute; left: 10px; top: 1016px; width: 190px; height: 84px;
    background: linear-gradient(to right, var(--placeholder-a), var(--placeholder-b));
  }
</style>
</head>
<body>
  <main class="poster">
    <div class="line today">TODAY<span class="is">IS ...</span></div>

    <div class="line just">JUST<span class="rest">Another Day For You</span></div>

    <svg class="divider" viewBox="0 0 590 6" aria-hidden="true">
      <line x1="0" y1="3" x2="590" y2="3" stroke="var(--dash)" stroke-width="3" stroke-dasharray="12 14"/>
    </svg>

    <div class="line most">THE MOST</div>
    <div class="line important">IMPORTANT DAY</div>
    <div class="line life">In Their Life</div>

    <div class="brand"><span class="mark"></span><span>Ridgeway<br>Haul Academy</span></div>

    <svg class="stripes" viewBox="0 0 882 72" preserveAspectRatio="none" aria-hidden="true">
      <g fill="var(--stripe)">
        <rect x="210" y="0" width="22" height="72" opacity="0.6"/>
        <rect x="250" y="0" width="22" height="72" opacity="0.65"/>
        <rect x="290" y="0" width="22" height="72" opacity="0.7"/>
        <rect x="330" y="0" width="22" height="72" opacity="0.75"/>
        <rect x="370" y="0" width="22" height="72" opacity="0.8"/>
        <rect x="410" y="0" width="22" height="72" opacity="0.85"/>
        <rect x="450" y="0" width="22" height="72" opacity="0.9"/>
        <rect x="490" y="0" width="22" height="72"/>
        <rect x="530" y="0" width="22" height="72"/>
        <rect x="570" y="0" width="22" height="72"/>
        <rect x="610" y="0" width="22" height="72"/>
        <rect x="650" y="0" width="22" height="72"/>
        <rect x="690" y="0" width="22" height="72"/>
        <rect x="730" y="0" width="22" height="72"/>
        <rect x="770" y="0" width="22" height="72"/>
        <rect x="810" y="0" width="22" height="72"/>
        <rect x="850" y="0" width="22" height="72"/>
      </g>
    </svg>

    <div class="truck-art" role="img" aria-label="Illustration of a semi truck with a white trailer and red cab"></div>
  </main>
</body>
</html>
```